Design Tweak needed for a current site

Design on top of an existing quiz funnel

Ideally we would like to tweak what we have already built here (moving elements, styles, adding simple elements etc): http://offers.plumrivetdeals.com/can-you-save-on-car-insurance

The flow:
1) User lands on the quiz page
2) User answers X questions and moves through the flow
3) Calculating user results screen
4) User reaches a success screen, and is subsequently redirected

Keys to the design:
1) We need to emphasize the quiz title as that will drive engagement. In this case, this is a quiz to see if you might be eligible to save money on car insurance.

2) At the end of the quiz we need to make it very, very clear that the user is eligible for savings and that in order to complete the process they are being redirected to another page where they need to fill out a form. It is critical that the design communicates this very clearly... We can count down the time left until redirect and we can use any order of elements to make this point. I think our current design does a very bad job of this.

3) We want to have a "calculating" step so that it seems like the page is working in the background

Goals of the design:
1) Polished, high quality experience throughout
2) User is clearly prepared to be redirected to the conversion funnel/landing page at the end
3) User understands the value of completing the quiz

Target Market(s)

designers

Industry/Entity Type

Moving

Number of Pages Required

1 page

Font styles to use
Sans Serif

Colors

Designer to choose colors to be used in the design.

Requirements
Must have
• This quiz funnel is a template so while the current use case is for auto insurance, we would like a design that also would work in other contexts.
Should not have
• We don't want to materially change the core functionality of the quiz itself... redesigning any of the elements or interactions is encouraged though

```html
<!DOCTYPE html>
<html lang="en">
<head>
<meta charset="utf-8">
<title>PlumRivet – Car Insurance Quiz</title>
<link rel="stylesheet" href="https://fonts.googleapis.com/css2?family=Raleway:wght@400;500;600&family=Open+Sans:ital,wght@0,400;0,600;1,400&family=Montserrat:wght@500&display=swap">
<style>
  :root {
    --red: #d81e3f;
    --white: #ffffff;
    --ink: #111114;
    --panel: rgba(12, 12, 15, 0.84);
    --rule: rgba(255, 255, 255, 0.16);
    --muted-num: #c9c9cc;
    --icon-fill: rgba(255, 255, 255, 0.14);
  }
  * { box-sizing: border-box; margin: 0; padding: 0; }
  html, body { width: 1200px; height: 771px; overflow: hidden; }
  body {
    position: relative;
    background: #0d1016;
    color: var(--white);
    font-family: "Open Sans", Arial, sans-serif;
  }
  .backdrop {
    position: absolute; inset: 0;
    background:
      radial-gradient(ellipse 40% 60% at 92% 55%, rgba(200, 40, 70, 0.45), transparent 70%),
      radial-gradient(ellipse 35% 50% at 10% 80%, rgba(180, 40, 60, 0.3), transparent 70%),
      linear-gradient(180deg, #0f1a2c 0%, #161b24 30%, #2a2b33 70%, #3a3c44 100%);
  }
  .quiz-panel {
    position: absolute; left: 155px; top: 137px;
    width: 867px; height: 567px;
    background: var(--panel);
  }
  .brand {
    position: absolute; left: 0; top: 34px; width: 1200px;
    text-align: center;
  }
  .brand-mark {
    display: block; width: 66px; height: 66px; margin: 0 auto;
    border-radius: 50%; background: var(--red);
    border: 8px solid var(--ink);
  }
  .brand-name {
    display: block; margin-top: 2px; line-height: 40px;
    font-family: "Raleway", Arial, sans-serif; font-weight: 600;
    font-size: 35px; letter-spacing: 0.5px; color: var(--white);
  }
  .quiz-title {
    position: absolute; left: 0; top: 216px; width: 1200px;
    text-align: center; line-height: 36px;
    font-family: "Raleway", Arial, sans-serif; font-weight: 500;
    font-size: 22px; color: var(--white);
  }
  .quiz-title .label { color: var(--red); font-weight: 600; font-size: 29px; margin-right: 6px; }
  .quiz-intro {
    position: absolute; left: 303px; top: 266px; width: 594px; height: 38px;
    border-top: 1px solid var(--rule); border-bottom: 1px solid var(--rule);
    display: flex; align-items: center; justify-content: center;
    font-size: 14.5px; color: #f0f0f0;
  }
  .progress { position: absolute; left: 0; top: 345px; }
  .step-num {
    font-family: "Open Sans", Arial, sans-serif; font-style: italic;
    font-size: 42px; text-anchor: middle;
  }
  .question {
    position: absolute; left: 0; top: 479px; width: 1200px; text-align: center;
    line-height: 28px;
    font-family: "Montserrat", Arial, sans-serif; font-weight: 500; font-size: 20.5px;
  }
  .choice {
    position: absolute; top: 558px; text-align: center;
  }
  .choice-icon {
    display: block; margin: 0 auto; height: 48px;
    background: var(--icon-fill); border-radius: 4px;
  }
  .choice-label {
    display: block; margin-top: 12px; padding-top: 8px;
    border-top: 1px solid var(--rule); font-size: 14.5px; line-height: 20px;
  }
  .choice.is-hover .choice-label { color: var(--red); }
  .sedan { left: 317px; width: 153px; }
  .sedan .choice-icon { width: 142px; }
  .suv { left: 551px; width: 111px; }
  .suv .choice-icon { width: 96px; }
  .other { left: 753px; width: 129px; }
  .other .choice-icon { width: 115px; }
</style>
</head>
<body>
  <div class="backdrop" role="img" aria-label="Night-time photo of a curving highway with red and white light trails"></div>

  <main class="quiz-panel"></main>

  <header class="brand">
    <span class="brand-mark"></span>
    <span class="brand-name">PlumRivet</span>
  </header>

  <h1 class="quiz-title"><span class="label">Quiz:</span>Are You Overpaying For Car Insurance?</h1>
  <p class="quiz-intro">Take our five question quiz to see if you might be eligible for car insurance savings</p>

  <svg class="progress" width="1200" height="100" viewBox="0 0 1200 100" aria-label="Step 2 of 5">
    <g stroke="#fff" stroke-width="2" fill="none">
      <line x1="300" y1="46" x2="372" y2="46"/><line x1="300" y1="54" x2="372" y2="54"/>
      <line x1="463" y1="46" x2="537" y2="46"/><line x1="463" y1="54" x2="537" y2="54"/>
      <line x1="628" y1="46" x2="708" y2="46"/><line x1="628" y1="54" x2="708" y2="54"/>
      <line x1="799" y1="46" x2="872" y2="46"/><line x1="799" y1="54" x2="872" y2="54"/>
    </g>
    <g stroke="#fff" stroke-width="2">
      <circle cx="254" cy="50" r="46" fill="var(--ink)"/>
      <circle cx="417" cy="50" r="46" fill="var(--ink)"/>
      <circle cx="582" cy="50" r="46" fill="var(--ink)"/>
      <circle cx="753" cy="50" r="46" fill="var(--ink)"/>
      <circle cx="917" cy="50" r="46" fill="var(--ink)"/>
    </g>
    <circle cx="254" cy="50" r="39" fill="var(--red)"/>
    <circle cx="417" cy="50" r="39" fill="var(--red)"/>
    <circle cx="582" cy="50" r="39" fill="#fff"/>
    <circle cx="753" cy="50" r="39" fill="#fff"/>
    <circle cx="917" cy="50" r="39" fill="#fff"/>
    <g fill="var(--red)">
      <path d="M292 44 L299 50 L292 56 Z"/>
      <path d="M455 44 L462 50 L455 56 Z"/>
    </g>
    <g fill="#fff">
      <path d="M620 44 L627 50 L620 56 Z"/>
      <path d="M791 44 L798 50 L791 56 Z"/>
    </g>
    <text class="step-num" x="252" y="65" fill="#fff">1</text>
    <text class="step-num" x="415" y="65" fill="#fff">2</text>
    <text class="step-num" x="580" y="65" fill="var(--muted-num)">3</text>
    <text class="step-num" x="751" y="65" fill="var(--muted-num)">4</text>
    <text class="step-num" x="915" y="65" fill="var(--muted-num)">5</text>
  </svg>

  <h2 class="question">2. What Kind of Car Do You Drive:</h2>

  <div class="choice sedan">
    <span class="choice-icon" role="img" aria-label="Outline illustration of a sedan"></span>
    <span class="choice-label">A Sedan</span>
  </div>

  <div class="choice suv is-hover">
    <span class="choice-icon" role="img" aria-label="Outline illustration of an SUV"></span>
    <span class="choice-label">An Suv</span>
  </div>

  <div class="choice other">
    <span class="choice-icon" role="img" aria-label="Outline illustration of a tanker truck with a plow"></span>
    <span class="choice-label">Other</span>
  </div>
</body>
</html>
```